Redesign our website!

Tandel’s current web (http://tandelwear.example) site was implemented in 2012 and needs to be brought up to date with look and feel of our new packaging and logo. The layout of Tandel’s website is fairly consistent from page to page; utilizing only two very similar “templates” or “themes.”

Project Description:
Tandel is seeking a designer to gain inspiration from our new packaging, design and recent print ad and create a new look for our website (http://tandelwear.example); focusing on the wallpaper, background, navigation bars/buttons, header and footer. Additionally, Tandel needs a new “style” for the images used in the slideshow on the homepage as well as the banner images on the product category/subcategory pages.

It is important that element height/width and positioning of elements (such as the "feature" boxes on the homepage, navigation bar, and banner images) within the pages are not changed in the new design. In other words, this project is solely focused on the overall design, not the specific layouts of each page.

Attached are:
* a zip file of JPEG examples of our new packaging;
* a pdf copy of a print ad we recently used for an industry tradeshow;
* a zip file with 2 JPEGS of images used in our booth at the above mentioned tradeshow;
* a JPEG of our new logo;
* a JPEG of the Background used on our new packing.

The model images that can be used in the mock-up of the new homepage slideshow but please do not feel as though you need to use the models in your banner mock-up. If you use your own models (stock images are OK,) please try to incorporate our products on the models.This will help us get a realistic sense of your direction.
Updates

I am very encouraged by the examples I am seeing. Thank you to those who have contributed and to those still working on it, please do! This is by no means a done deal with any one design.

One tip to those who have already contributed and those still to do so: we are looking for a new color scheme. Please do not use the brown/green you see on the current site.  Thank you.

Requirements
Must have
• Remove "Vines" from the background"
Change the header to less look "yoga"ish
1 "sample" image for the homepage slideshow
1 "sample image" for a category banner (i.e. the banner on http://tandelwear.example/wristos/)

```html
<!DOCTYPE html>
<html lang="en">
<head>
<meta charset="utf-8">
<title>Tandel — Home</title>
<link rel="stylesheet" href="https://fonts.googleapis.com/css2?family=Bebas+Neue&family=Play:wght@700&family=Roboto:wght@400;700&family=Roboto+Condensed&family=PT+Sans&family=Open+Sans:wght@400;700&display=swap">
<style>
:root{
  --orange:#ff6a00;
  --orange-dark:#e55c00;
  --topbar:#2f2f2f;
  --navbar:#3b3b3b;
  --nav-active:#1d1d1d;
  --divider:#2a2a2a;
  --light:#e6e7e8;
  --ink:#333;
  --footer:#262626;
  --footer-bottom:#1f1f1f;
  --footer-text:#c9c9c9;
  --red:#c8141b;
}
*{box-sizing:border-box;margin:0;padding:0}
html,body{width:1146px;height:1200px;overflow:hidden;background:#fff}
body{position:relative;font-family:"Open Sans",sans-serif}
.abs{position:absolute}

.topbar{left:0;top:0;width:1146px;height:43px;background:var(--topbar)}
.top-btn{top:10px;height:31px;background:#3d3d3d;border:1px solid #222;color:#ddd;white-space:nowrap;
  font:11px "Roboto Condensed",sans-serif;display:flex;align-items:center;gap:5px;padding:0 8px}
.login{left:561px;width:117px}
.cart{left:688px;width:109px}
.cart-total{left:797px;width:36px;background:#555;justify-content:center;padding:0}
.badge{left:687px;top:7px;width:16px;height:16px;border-radius:50%;background:#1a8fd6;color:#fff;
  font:9px "Roboto",sans-serif;display:flex;align-items:center;justify-content:center}
.search{left:844px;width:180px;justify-content:space-between;color:#999;background:#474747}

.navbar{left:0;top:43px;width:1146px;height:86px;background:var(--navbar);border-bottom:3px solid #2c2c2c}
.logo{left:122px;top:58px;font:400 52px "Roboto",sans-serif;color:#d8d8d8;letter-spacing:-1px}
.logo-dot{left:268px;top:74px;width:8px;height:8px;border:1px solid #d8d8d8;border-radius:50%}
.nav-item{top:43px;height:86px;border-left:1px solid var(--divider);display:flex;flex-direction:column;
  align-items:center;justify-content:center;color:#fff;font:700 16px "Roboto",sans-serif}
.nav-item small{font-size:9px;color:#ddd;margin-top:1px}
.nav-item.active{background:var(--nav-active);color:var(--orange)}

.hero{left:0;top:131px;width:1146px;height:401px;
  background:radial-gradient(ellipse 420px 330px at 560px 170px,#8a8a8a 0%,#4a4a4a 45%,#111 85%,#000 100%)}
.hero-photo{left:385px;top:131px;width:340px;height:401px;
  background:linear-gradient(180deg,#caa08a 0%,#e9c3c6 55%,#2e3355 100%);border-radius:0 0 40px 40px}
.hero-title{left:105px;top:246px;width:331px;height:56px;background:#000;color:#fff;
  font:700 34px "Play",sans-serif;padding:7px 0 0 22px}
.hero-sub{left:105px;top:302px;width:331px;height:39px;background:var(--orange);color:#fff;
  font:700 13px "Open Sans",sans-serif;padding:10px 0 0 20px}
.social{left:836px;width:34px;height:34px;background:#2a2a2a;border:1px solid #555}

.feature{top:568px;width:289px;height:315px;background:var(--light);text-align:center}
.feature.hot{background:var(--orange)}
.feature-img{position:absolute;left:20px;top:15px;width:249px;height:114px;border:5px solid #d2d2d2;
  box-shadow:0 6px 6px -3px rgba(0,0,0,.5)}
.feature.hot .feature-img{border-color:#e2e2e2}
.feature h2{position:absolute;left:0;right:0;top:157px;font:400 27px "Bebas Neue",sans-serif;color:var(--ink);letter-spacing:.3px}
.feature.hot h2{color:#fff}
.feature p{position:absolute;left:20px;right:16px;top:195px;text-align:left;font:11px/16.5px "Open Sans",sans-serif;color:#444;letter-spacing:.2px}
.feature.hot p{color:#fff}
.btn{position:absolute;left:50%;transform:translateX(-50%);top:253px;width:106px;height:37px;
  background:linear-gradient(#333,#000);border-radius:3px;color:#fff;font:400 21px/38px "Bebas Neue",sans-serif}
.feature.hot .btn{background:linear-gradient(#e8262d,#b10f15)}

.shadow-line{left:113px;top:910px;width:920px;height:10px;
  background:radial-gradient(ellipse 50% 60% at 50% 0%,rgba(0,0,0,.14),transparent)}

.footer{left:0;top:945px;width:1146px;height:210px;background:var(--footer);border-top:3px solid var(--orange)}
.footer-bottom{left:0;top:1155px;width:1146px;height:45px;background:var(--footer-bottom)}
.f-head{top:988px;font:15px "Roboto Condensed",sans-serif;color:var(--orange);letter-spacing:.5px}
.f-rule{top:1014px;height:1px;background:#3c3c3c}
.f-list{list-style:none;font:13px "PT Sans",sans-serif;color:var(--footer-text)}
.f-list li{height:25.5px}
.f-list li::before{content:"»";color:var(--orange);font-size:9px;margin-right:10px;vertical-align:2px}
.addr{left:442px;top:1028px;font:13px/25.5px "PT Sans",sans-serif;color:var(--footer-text)}
.contact{left:623px;font:13px "PT Sans",sans-serif;color:var(--footer-text);display:flex;align-items:center;gap:8px}
.f-social{top:1096px;width:22px;height:22px;background:#555;border:1px solid #777}
.newsletter{left:802px;top:990px;width:230px;font:12.5px/16px "PT Sans",sans-serif;color:var(--footer-text)}
.email{left:800px;top:1083px;width:177px;height:37px;background:#2e2e2e;border:1px solid #444;
  color:#bbb;font:14px/35px "PT Sans",sans-serif;padding-left:10px}
.go{left:977px;top:1083px;width:47px;height:37px;background:var(--orange);border:1px solid #f9a160;
  color:#fff;font:400 24px/38px "Bebas Neue",sans-serif;text-align:center}
.f-brand{left:122px;top:1160px;display:flex;align-items:baseline;gap:8px;white-space:nowrap}
.f-logo{font:400 30px "Roboto",sans-serif;color:#9a9a9a;letter-spacing:-.5px}
.copy{font:11px "PT Sans",sans-serif;color:#8a8a8a}
</style>
</head>
<body>

<div class="abs topbar"></div>
<div class="abs top-btn login">
  <svg width="13" height="13" viewBox="0 0 14 14"><circle cx="7" cy="4" r="3.2" fill="#ccc"/><path d="M1 14c0-4 3-6 6-6s6 2 6 6z" fill="#ccc"/></svg>
  LOGIN / REGISTER
</div>
<div class="abs top-btn cart">
  <svg width="15" height="12" viewBox="0 0 16 13"><path d="M0 1h3l2 7h8l2-5H4" fill="none" stroke="#ccc" stroke-width="1.5"/><circle cx="6" cy="11" r="1.4" fill="#ccc"/><circle cx="12" cy="11" r="1.4" fill="#ccc"/></svg>
  SHOPPING CART
</div>
<div class="abs top-btn cart-total">$0.00</div>
<div class="abs badge">0</div>
<div class="abs top-btn search">Search...
  <svg width="14" height="14" viewBox="0 0 14 14"><circle cx="5.5" cy="5.5" r="4.2" fill="none" stroke="#eee" stroke-width="2"/><path d="M8.5 8.5l4.5 4.5" stroke="#eee" stroke-width="2.4"/></svg>
</div>

<div class="abs navbar"></div>
<div class="abs logo">Tandel</div>
<div class="abs logo-dot"></div>
<div class="abs nav-item active" style="left:301px;width:77px">HOME</div>
<div class="abs nav-item" style="left:379px;width:124px">WRISTOS<small>WRIST WALLETS</small></div>
<div class="abs nav-item" style="left:503px;width:115px">EARCOZIES<small>EAR WARMERS</small></div>
<div class="abs nav-item" style="left:618px;width:108px">APPAREL</div>
<div class="abs nav-item" style="left:726px;width:146px">ACCESSORIES</div>
<div class="abs nav-item" style="left:872px;width:150px;border-right:1px solid var(--divider)">ECO PRODUCTS</div>

<div class="abs hero"></div>
<div class="abs hero-photo" role="img" aria-label="Smiling woman in a pink scarf wearing a wrist wallet, against a dark textured wall"></div>
<div class="abs hero-title">Find Within</div>
<div class="abs hero-sub">Lorem ipsum dolor et le protechimpa detelere</div>
<div class="abs social" style="top:177px"></div>
<div class="abs social" style="top:218px"></div>
<div class="abs social" style="top:261px"></div>
<div class="abs social" style="top:306px"></div>

<div class="abs feature" style="left:117px">
  <div class="feature-img" role="img" aria-label="Man with earphones wearing a black wrist wallet" style="background:linear-gradient(90deg,#d9d9d9,#bcbcbc)"></div>
  <h2>LOOK AT THAT!</h2>
  <p>Lorem ipsum dolor et me mensaje del a la nula estaba en la dolor.&nbsp; No em mehidian delibah meiserelifereba en tu model.</p>
  <div class="btn">READ MORE</div>
</div>
<div class="abs feature" style="left:427px">
  <div class="feature-img" role="img" aria-label="Two runners jogging along a lakeside" style="background:linear-gradient(180deg,#dfe6ec 0%,#8e9da5 45%,#7a8d4a 100%)"></div>
  <h2>YOU CAN TAKE IT WITH YOU</h2>
  <p>Lorem ipsum dolor et me mensaje del a la nula estaba en la dolor.&nbsp; No em mehidian delibah meiserelifereba en tu model.</p>
  <div class="btn">READ MORE</div>
</div>
<div class="abs feature hot" style="left:740px">
  <div class="feature-img" role="img" aria-label="Smiling man outdoors wearing a colourful wrist wallet" style="background:linear-gradient(90deg,#6b5a4a,#a9a9a0)"></div>
  <h2>WRISTOS WRIST WALLETS</h2>
  <p>Lorem ipsum dolor et me mensaje del a la nula estaba en la dolor.&nbsp; No em mehidian delibah meiserelifereba en tu model.</p>
  <div class="btn">READ MORE</div>
</div>

<div class="abs shadow-line"></div>

<div class="abs footer"></div>
<div class="abs footer-bottom"></div>

<div class="abs f-head" style="left:123px">HELP LINKS</div>
<div class="abs f-rule" style="left:123px;width:257px"></div>
<ul class="abs f-list" style="left:125px;top:1028px">
  <li>Advocates &amp;</li><li>Affiliate Program</li><li>Back Story</li><li>News</li>
</ul>
<ul class="abs f-list" style="left:284px;top:1028px">
  <li>About Us</li><li>Press / Media</li><li>Contact Us</li><li>FAQS</li>
</ul>

<div class="abs f-head" style="left:442px">HOW TO FIND US</div>
<div class="abs f-rule" style="left:442px;width:128px"></div>
<div class="abs addr">TANDEL<br>12 Alder Lane<br>Brookfield, New<br>York 10500</div>

<div class="abs f-head" style="left:623px">CONTACTS</div>
<div class="abs f-rule" style="left:623px;width:128px"></div>
<div class="abs contact" style="top:1035px">
  <svg width="16" height="18" viewBox="0 0 16 18"><path d="M3 1l3 4-2 2c1 3 3 5 6 7l2-2 3 3-2 3C7 17 1 10 1 3z" fill="#bbb"/></svg>
  555-010-4421
</div>
<div class="abs contact" style="top:1063px">
  <svg width="16" height="16" viewBox="0 0 16 16"><rect x="4" y="1" width="8" height="4" fill="#bbb"/><rect x="1" y="6" width="14" height="6" rx="1" fill="#bbb"/><rect x="4" y="11" width="8" height="4" fill="#888"/></svg>
  555-010-4422
</div>
<div class="abs f-social" style="left:622px"></div>
<div class="abs f-social" style="left:649px"></div>
<div class="abs f-social" style="left:676px"></div>
<div class="abs f-social" style="left:703px"></div>

<div class="abs newsletter">Sign up to our Newsletter and receive occasional e-mail updates about new features and special offers from our company.</div>
<div class="abs email">Email address</div>
<div class="abs go">GO!</div>

<div class="abs f-brand">
  <span class="f-logo">Tandel</span>
  <span class="copy">Copyright © 2013.&nbsp; All Rights Reserved.</span>
</div>

</body>
</html>
```